Attractive Wall Posters wanted

We are designing posters for our outdoor wall to represent our brands.

(Portrait Layout: Measurements - Height 128cm, Width 108cm).

More information for each brand can be found on the website listed in the ppt attached.

Requirements
Must have
• The information included in PPT, the logo, the website and the short description
Nice to have
• Consistency across all posters
Should not have
• too cluttered designs

```html
<!DOCTYPE html>
<html lang="en">
<head>
<meta charset="utf-8">
<title>Lumen Foundation – Social Enterprise Poster</title>
<link href="https://fonts.googleapis.com/css2?family=Arimo:wght@400;700&display=swap" rel="stylesheet">
<style>
  :root {
    --green: #9bbb2e;
    --green-dark: #86a623;
    --button: #b2cb5c;
    --pale: #eaf0d4;
    --white: #ffffff;
    --ink: #1c1c1c;
    --sky: #cfe3ef;
    --crowd: #8fae3a;
  }
  html, body { margin: 0; padding: 0; overflow: hidden; background: var(--white); }
  .poster {
    position: relative; width: 1013px; height: 1200px; overflow: hidden;
    background: var(--white); font-family: "Arimo", Arial, sans-serif; color: var(--ink);
  }
  .top-band { position: absolute; left: 0; top: 24px; width: 1013px; height: 216px; background: var(--pale); }
  .bottom-band { position: absolute; left: 0; top: 860px; width: 1013px; height: 340px; background: var(--pale); }

  .brand { position: absolute; left: 48px; top: 40px; width: 230px; text-align: center; }
  .brand-circle {
    width: 120px; height: 120px; margin: 0 auto 18px; border-radius: 50%;
    border: 6px solid var(--green); background: var(--white);
  }
  .brand-name { font-weight: 700; font-size: 27px; color: var(--green); letter-spacing: 0.5px; }

  .hero-dot { position: absolute; left: 730px; top: 20px; width: 68px; height: 68px; border-radius: 50%; background: var(--green); }
  .hero-ring {
    position: absolute; left: 748px; top: 16px; width: 232px; height: 232px; border-radius: 50%;
    background: var(--green); box-shadow: 0 2px 6px rgba(0,0,0,.35);
  }
  .hero-photo {
    position: absolute; left: 18px; top: 18px; width: 196px; height: 196px; border-radius: 50%;
    background: radial-gradient(circle at 50% 55%, #d9cfb7 0%, #9a8e79 45%, #3b3a36 100%);
  }

  .intro { position: absolute; left: 40px; top: 284px; width: 520px; }
  .intro h2 { margin: 0 0 22px 2px; font-size: 25px; font-weight: 700; color: var(--green); }
  .intro p { margin: 0 0 24px; font-size: 19px; line-height: 26px; text-align: justify; }

  .actions { position: absolute; left: 662px; top: 294px; width: 272px; }
  .action {
    display: flex; align-items: center; height: 62px; margin-bottom: 40px; padding-left: 14px;
    background: var(--button); color: var(--white); font-size: 21px; letter-spacing: 0.6px;
    box-shadow: 2px 3px 4px rgba(0,0,0,.35); text-transform: uppercase;
  }
  .action svg { width: 24px; height: 30px; margin-right: 10px; flex: none; }

  .wave { position: absolute; left: 0; top: 530px; width: 1013px; height: 430px; }

  .moment-ring {
    position: absolute; left: 706px; top: 884px; width: 262px; height: 262px; border-radius: 50%;
    background: var(--white); box-shadow: 0 2px 8px rgba(0,0,0,.35);
  }
  .moment-photo {
    position: absolute; left: 9px; top: 9px; width: 244px; height: 244px; border-radius: 50%;
    background: linear-gradient(180deg, #c9c6c4 0%, #8b8180 45%, #3d3a3d 80%, #f1eef0 100%);
  }

  .program { position: absolute; left: 50px; top: 980px; display: flex; align-items: center; gap: 10px; }
  .program-dot { width: 40px; height: 40px; border-radius: 50%; background: #b9a88a; }
  .program-name { font-size: 20px; font-weight: 700; color: #a9a17a; }

  .quote { position: absolute; left: 262px; top: 976px; width: 240px; margin: 0; font-size: 23px; line-height: 29px; text-align: justify; }
  .quote .mark { color: var(--green); font-weight: 700; }

  .discover { position: absolute; left: 50px; top: 1128px; margin: 0; font-size: 21px; }
  .discover .url { color: var(--green); font-weight: 700; }
</style>
</head>
<body>
<div class="poster">
  <div class="top-band"></div>
  <div class="bottom-band"></div>

  <div class="brand">
    <div class="brand-circle"></div>
    <div class="brand-name">LUMEN FOUNDATION</div>
  </div>

  <div class="hero-ring">
    <div class="hero-photo" role="img" aria-label="Photo of young people working together around a table with learning cards"></div>
  </div>
  <div class="hero-dot"></div>

  <section class="intro">
    <h2>Social Enterprise</h2>
    <p>Lumen Foundation is born out of a desire to contribute in a different way towards inspiring youth in developing countries. We train talents with our time.</p>
    <p>Through a Learn 1 Give 1 concept, we seek to involve speakers, trainers as well as volunteers to contribute their time towards training talents.</p>
  </section>

  <nav class="actions">
    <div class="action"><svg viewBox="0 0 24 30"><path d="M3 2 L19 15 L3 28" fill="none" stroke="#fff" stroke-width="5"/></svg>Need help?</div>
    <div class="action"><svg viewBox="0 0 24 30"><path d="M3 2 L19 15 L3 28" fill="none" stroke="#fff" stroke-width="5"/></svg>Be a volunteer</div>
    <div class="action"><svg viewBox="0 0 24 30"><path d="M3 2 L19 15 L3 28" fill="none" stroke="#fff" stroke-width="5"/></svg>Support us</div>
  </nav>

  <svg class="wave" viewBox="0 0 1013 430" aria-hidden="false">
    <defs>
      <linearGradient id="crowdTone" x1="0" y1="0" x2="0" y2="1">
        <stop offset="0" stop-color="var(--sky)"/>
        <stop offset="0.35" stop-color="#b9cdb3"/>
        <stop offset="0.6" stop-color="var(--crowd)"/>
        <stop offset="1" stop-color="#4e5a2e"/>
      </linearGradient>
    </defs>
    <path role="img" aria-label="Group photo of volunteers in green shirts forming letters with their arms outdoors"
          d="M0 80 C110 30 220 18 320 28 C520 50 720 120 1013 72 L1013 355 C900 395 720 425 540 418 C360 410 180 340 0 340 Z"
          fill="url(#crowdTone)"/>
    <path d="M290 12 C520 30 730 100 1013 25 L1013 72 C730 125 520 60 290 12 Z" fill="var(--green)"/>
    <path d="M0 328 C190 322 370 398 560 420 C370 424 180 372 0 372 Z" fill="var(--green)"/>
  </svg>

  <div class="moment-ring">
    <div class="moment-photo" role="img" aria-label="Photo of a cheering group of students raising their hands at an award ceremony"></div>
  </div>

  <div class="program">
    <div class="program-dot"></div>
    <div class="program-name">LEARN 1 GIVE 1</div>
  </div>

  <p class="quote"><span class="mark">“</span>If you treasure time, there is no greater gift than to give it away.<span class="mark">”</span></p>

  <p class="discover">Discover more at: <span class="url">www.lumenfoundation.org</span></p>
</div>
</body>
</html>
```